Tour agency for FIT and groups need a business card design

We need a business card design for a tour agency company that is based in Perth called" BRISK NO", we aim to provide customise, unique and seamless travel arrangement for FIT and groups. We serve both high profile businessperson, government authorities, business partners, executives and investors. The name card should be more professional looking.
Updates

Project Deadline Extended Reason: Have some changes that needed to make, director will be back to office on Monday, sorry for the inconvenience cause. Added Saturday, May 6, 2017

Target Market(s)

High profile businessperson, government authorities, business partners, executives and investors.

Industry/Entity Type

Tourism

Contact Information for Business Card

Brisk NO
Level 1, 214 Marlowe Avenue, Dunreath NO, 6120
www.briskno.com.au

Font styles to use
Serif

Colors

Designer to choose colors to be used in the design.

Requirements
Must have
• My project must have a company logo
Nice to have
• a more professional and solid yet friendly name card design. We may want to include chinese name in the name card as well. Edge of the card can be filled with gold and we think that transparent name cards are interesting.

```html
<!DOCTYPE html>
<html lang="en">
<head>
<meta charset="utf-8">
<title>Brisk NO — Business Card</title>
<link href="https://fonts.googleapis.com/css2?family=Lato:wght@400;700&family=Raleway:ital,wght@1,700&display=swap" rel="stylesheet">
<style>
  :root {
    --backdrop: #2e2f31;
    --card: #ffffff;
    --brand-blue: #23a6dd;
    --ink: #1b1b1b;
    --ink-soft: #333333;
  }
  html, body {
    margin: 0;
    padding: 0;
    width: 1200px;
    height: 1200px;
    overflow: hidden;
    background: var(--backdrop);
    font-family: "Lato", sans-serif;
  }
  .canvas { position: relative; width: 1200px; height: 1200px; }
  .card {
    position: absolute;
    left: 174px;
    width: 816px;
    height: 490px;
    background: var(--card);
    box-shadow: 0 4px 10px rgba(0,0,0,0.45);
  }
  .card--front { top: 101px; }
  .card--back { top: 612px; }

  .ribbon {
    position: absolute;
    left: 0;
    top: 97px;
    width: 386px;
    height: 70px;
  }
  .ribbon svg { position: absolute; inset: 0; }
  .ribbon__text {
    position: absolute;
    left: 16px;
    top: 0;
    line-height: 70px;
    font-family: "Raleway", sans-serif;
    font-style: italic;
    font-weight: 700;
    font-size: 29px;
    color: #fff;
    letter-spacing: 0.2px;
  }

  .brand-mark {
    position: absolute;
    display: flex;
    align-items: center;
    gap: 14px;
    font-family: "Lato", sans-serif;
    font-weight: 700;
    color: var(--brand-blue);
    white-space: nowrap;
  }
  .brand-mark__dot {
    border-radius: 50%;
    background: var(--brand-blue);
    flex: none;
  }
  .card--front .brand-mark { left: 378px; top: 310px; font-size: 66px; }
  .card--front .brand-mark__dot { width: 26px; height: 26px; }
  .card--back .brand-mark { left: 488px; top: 96px; font-size: 56px; }
  .card--back .brand-mark__dot { width: 22px; height: 22px; }

  .holder__name {
    position: absolute;
    left: 44px;
    top: 186px;
    margin: 0;
    font-size: 39px;
    font-weight: 700;
    color: var(--ink);
  }
  .holder__role {
    position: absolute;
    left: 48px;
    top: 237px;
    font-size: 20px;
    color: var(--ink-soft);
  }
  .holder__rule {
    position: absolute;
    left: 98px;
    top: 254px;
    width: 672px;
    height: 2px;
    background: var(--brand-blue);
  }

  .contact-list {
    position: absolute;
    left: 46px;
    top: 288px;
    margin: 0;
    padding: 0;
    list-style: none;
  }
  .contact-list li {
    display: flex;
    align-items: center;
    height: 28px;
    margin-bottom: 13px;
    font-size: 20px;
    color: var(--ink-soft);
  }
  .contact-list svg { width: 20px; height: 20px; margin-right: 14px; flex: none; }
</style>
</head>
<body>
<div class="canvas">

  <section class="card card--front">
    <div class="ribbon">
      <svg width="386" height="70" viewBox="0 0 386 70" aria-hidden="true">
        <polygon points="0,0 386,0 362,35 386,70 0,70" fill="var(--brand-blue)"/>
      </svg>
      <span class="ribbon__text">www.briskno.com.au</span>
    </div>
    <div class="brand-mark"><span class="brand-mark__dot"></span>Brisk NO</div>
  </section>

  <section class="card card--back">
    <div class="brand-mark"><span class="brand-mark__dot"></span>Brisk NO</div>

    <h1 class="holder__name">Dean Halloway</h1>
    <span class="holder__role">Pilot</span>
    <div class="holder__rule"></div>

    <ul class="contact-list">
      <li>
        <svg viewBox="0 0 24 24" aria-hidden="true"><path fill="var(--brand-blue)" d="M6.6 10.8a15.1 15.1 0 0 0 6.6 6.6l2.2-2.2c.3-.3.7-.4 1-.2 1.1.4 2.3.6 3.6.6.6 0 1 .4 1 1V20c0 .6-.4 1-1 1A17 17 0 0 1 3 4c0-.6.4-1 1-1h3.5c.6 0 1 .4 1 1 0 1.3.2 2.5.6 3.6.1.3 0 .7-.2 1z"/></svg>
        00000-000000
      </li>
      <li>
        <svg viewBox="0 0 24 24" aria-hidden="true"><rect x="2" y="5" width="20" height="14" rx="1" fill="var(--brand-blue)"/><path d="M2.5 5.5 12 13l9.5-7.5M2.5 18.5l7-6M21.5 18.5l-7-6" stroke="#fff" stroke-width="1.5" fill="none"/></svg>
        info@example.com
      </li>
      <li>
        <svg viewBox="0 0 24 24" aria-hidden="true"><g fill="none" stroke="var(--brand-blue)" stroke-width="1.4"><circle cx="12" cy="12" r="9.5"/><ellipse cx="12" cy="12" rx="4.5" ry="9.5"/><path d="M2.5 12h19M4 7h16M4 17h16M12 2.5v19"/></g></svg>
        www.briskno.com.au
      </li>
      <li>
        <svg viewBox="0 0 24 24" aria-hidden="true"><path fill="var(--brand-blue)" d="M12 1.5a7 7 0 0 0-7 7c0 5.2 7 14 7 14s7-8.8 7-14a7 7 0 0 0-7-7zm0 9.7a2.7 2.7 0 1 1 0-5.4 2.7 2.7 0 0 1 0 5.4z"/></svg>
        Level 1, 214 Marlowe Avenue, Dunreath NO, 6120
      </li>
    </ul>
  </section>

</div>
</body>
</html>
```